Corvane Real Estate Business Card

hello, we are a real estate company located in Los Angeles, california. we are a boutique, small company but we like a big corportate look. a simple, sleek, modern and progressive look. we would like the option of having a design that could include the real estate agents personal photo and also a design if the realtor desides not to have a photo. We also would like a hotizontal design.

Corvane Properties
3817 S Hadderly
Ashgrove Heights, CA 90917
www.CorvaneRE.example

Gavin Prosk
Broker
BRE # 04829176
(555) 274-6390
gavin@corvanere.example

```html
<!DOCTYPE html>
<html lang="en">
<head>
<meta charset="utf-8">
<title>Corvane Properties – Business Card</title>
<link href="https://fonts.googleapis.com/css2?family=Roboto:wght@300;400;500&display=swap" rel="stylesheet">
<style>
  :root {
    --backdrop: #e9e9ea;
    --brand-deep: #17548f;
    --brand-mid: #2a6ea6;
    --brand-light: #4585b0;
    --panel-top: #1b5d9c;
    --panel-bottom: #0f417c;
    --ink-blue: #1f6aa6;
    --accent-blue: #4a9ad6;
    --paper: #fbfbfa;
    --white: #ffffff;
  }
  * { box-sizing: border-box; margin: 0; padding: 0; }
  html, body { width: 1200px; height: 720px; overflow: hidden; }
  body {
    background: var(--backdrop);
    font-family: "Roboto", Arial, sans-serif;
    position: relative;
  }
  .card {
    position: absolute;
    top: 241px;
    width: 420px;
    height: 240px;
    overflow: hidden;
  }

  /* Front side */
  .card-front {
    left: 147px;
    background: linear-gradient(200deg, var(--brand-light) 0%, var(--brand-mid) 45%, var(--brand-deep) 100%);
    color: var(--white);
  }
  .front-brand {
    position: absolute;
    left: 42px;
    top: 86px;
    display: flex;
    align-items: center;
    gap: 14px;
  }
  .brand-dot {
    width: 44px;
    height: 44px;
    border-radius: 50%;
    background: var(--white);
  }
  .front-brand .brand-name {
    font-weight: 300;
    font-size: 60px;
    line-height: 1;
    letter-spacing: -1px;
  }
  .front-tagline {
    position: absolute;
    right: 55px;
    top: 149px;
    font-weight: 300;
    font-size: 14px;
    letter-spacing: 1.5px;
    opacity: .85;
  }
  .front-url {
    position: absolute;
    left: 0;
    right: 0;
    top: 214px;
    text-align: center;
    font-size: 11px;
    letter-spacing: 3px;
    font-weight: 400;
  }

  /* Back side */
  .card-back {
    left: 633px;
    background: var(--paper);
    display: flex;
  }
  .back-info {
    position: relative;
    width: 251px;
    height: 100%;
  }
  .back-brand {
    position: absolute;
    left: 15px;
    top: 38px;
    color: var(--ink-blue);
  }
  .back-brand-row {
    display: flex;
    align-items: center;
    gap: 8px;
  }
  .back-brand .brand-dot {
    width: 24px;
    height: 24px;
    background: var(--ink-blue);
  }
  .back-brand .brand-name {
    font-weight: 400;
    font-size: 36px;
    line-height: 1;
    letter-spacing: -.5px;
  }
  .back-brand .brand-sub {
    display: block;
    text-align: right;
    font-size: 8px;
    letter-spacing: .8px;
    color: var(--accent-blue);
    margin-top: 1px;
    padding-right: 4px;
  }
  .address {
    position: absolute;
    left: 10px;
    top: 128px;
    display: flex;
    gap: 6px;
    color: var(--accent-blue);
    font-size: 13px;
    line-height: 20px;
  }
  .address svg { margin-top: 3px; flex: none; }

  .agent-panel {
    position: relative;
    width: 169px;
    height: 100%;
    background: linear-gradient(180deg, var(--panel-top), var(--panel-bottom));
    color: var(--white);
    text-align: center;
  }
  .portrait-ring {
    position: absolute;
    left: 20px;
    top: 15px;
  }
  .agent-details {
    position: absolute;
    left: 0;
    right: 0;
    top: 147px;
  }
  .agent-name { font-size: 13px; font-weight: 500; line-height: 16px; }
  .agent-role { font-size: 11.5px; line-height: 15px; margin-bottom: 6px; }
  .agent-contact { font-size: 10px; line-height: 12.5px; }
  .agent-email { margin-top: 2px; }
</style>
</head>
<body>

  <section class="card card-front" aria-label="Business card front">
    <div class="front-brand">
      <span class="brand-dot"></span>
      <span class="brand-name">corvane</span>
    </div>
    <div class="front-tagline">PROPERTIES</div>
    <div class="front-url">www.CorvaneRE.example</div>
  </section>

  <section class="card card-back" aria-label="Business card back">
    <div class="back-info">
      <div class="back-brand">
        <div class="back-brand-row">
          <span class="brand-dot"></span>
          <span class="brand-name">corvane</span>
        </div>
        <span class="brand-sub">PROPERTIES</span>
      </div>
      <div class="address">
        <svg width="11" height="14" viewBox="0 0 11 14" aria-hidden="true">
          <path d="M5.5 0C2.5 0 0 2.4 0 5.4 0 9.2 5.5 14 5.5 14S11 9.2 11 5.4C11 2.4 8.5 0 5.5 0z" fill="var(--ink-blue)"/>
          <circle cx="5.5" cy="5.3" r="2" fill="var(--paper)"/>
        </svg>
        <p>3817 S Hadderly<br>Ashgrove Heights, CA 90917</p>
      </div>
    </div>

    <div class="agent-panel">
      <svg class="portrait-ring" width="130" height="130" viewBox="0 0 130 130">
        <defs>
          <radialGradient id="portrait-tone" cx="50%" cy="40%" r="60%">
            <stop offset="0" stop-color="#c9a58a"/>
            <stop offset=".6" stop-color="#8a7a68"/>
            <stop offset="1" stop-color="#3e4a4c"/>
          </radialGradient>
        </defs>
        <circle cx="65" cy="65" r="64" fill="none" stroke="#3f8fd0" stroke-width="1.5" opacity=".8"/>
        <circle cx="65" cy="65" r="60" fill="#164c88"/>
        <circle cx="65" cy="65" r="54" fill="url(#portrait-tone)" role="img" aria-label="Agent portrait photo"/>
        <circle cx="117" cy="30" r="2.5" fill="#9fd4ff"/>
      </svg>
      <div class="agent-details">
        <p class="agent-name">Gavin Prosk</p>
        <p class="agent-role">Broker</p>
        <p class="agent-contact">BRE # 04829176<br>(555) 274-6390</p>
        <p class="agent-contact agent-email">gavin@corvanere.example</p>
      </div>
    </div>
  </section>

</body>
</html>
```